Executive search firm in fashion, luxury and retail industry needs logo and card design.

We are a start-up recruiting firm that specializes in the retail and fashion industry, based in New York. We are looking for something that will appeal to CEO level clients and candidates, but that has a little design edge...not overly corporate but still CEO-appropriate. We have clean, sophisticated taste and want a contemporary feel. Happy to have a two sided card. Not afraid of a little color but it should be high-design, not gimmicky and tasteful.

Quillmart Market(s)

CEO's, HR Leaders, in retail, fashion (i.e. Halvorsen, Quillmart, Otto Brevik)

Industry/Entity Type

Professional Service

Contact Information for Business Card

Calloway Ridge Search Partners
Address to be determined
New York, NY 10036

Marta Velard
Managing Director
(555)038-4172
mvelard@callowayridgesearch.example

Font styles to use
Serif
Sans Serif

Requirements
Must have
• clean lines, crisp graphics, some color. Prefer a graphic treatment over a "logo" per se. No pictures, etc.
Nice to have
• double sided design.
Should not have
• Gimmicks, smaltz, goop. Think Gallery of Current Works, not the Dunmore Holdings. No earth tones, as in beige and brown, no pastels. Strong colors are fine in moderation. Grays are good. Jewel tones are good. No red.

```html
<!DOCTYPE html>
<html lang="en">
<head>
<meta charset="utf-8">
<title>Marta Velard — Business Card</title>
<link rel="stylesheet" href="https://fonts.googleapis.com/css2?family=Arimo:wght@400&display=swap">
<style>
  :root {
    --ink: #010605;
    --stripe-mid: #717171;
    --stripe-light: #efefef;
    --stripe-dark: #2d2d2d;
    --band-green: #97b95a;
    --text-light: #ffffff;
    --text-dark: #0a0a0a;
  }
  html, body {
    margin: 0;
    padding: 0;
    width: 1200px;
    height: 790px;
    overflow: hidden;
    background: var(--ink);
  }
  .card {
    position: relative;
    width: 1200px;
    height: 790px;
    background: var(--ink);
    font-family: "Arimo", Arial, sans-serif;
    overflow: hidden;
  }
  .stripe {
    position: absolute;
    top: 0;
    height: 790px;
  }
  .stripe--mid   { left: 146px; width: 136px; background: var(--stripe-mid); }
  .stripe--light { left: 315px; width: 52px;  background: var(--stripe-light); }
  .stripe--dark  { left: 775px; width: 300px; background: var(--stripe-dark); }
  .band {
    position: absolute;
    left: 0;
    top: 461px;
    width: 1200px;
    height: 120px;
    background: var(--band-green);
  }
  .name {
    position: absolute;
    right: 135px;
    top: 372px;
    margin: 0;
    margin-right: -11px;
    font-weight: 400;
    font-size: 72px;
    line-height: 1;
    letter-spacing: 11px;
    color: var(--text-light);
    white-space: nowrap;
  }
  .address {
    position: absolute;
    left: 151px;
    top: 472px;
    margin: 0;
    font-size: 24px;
    line-height: 31px;
    letter-spacing: 4.6px;
    color: var(--text-dark);
    font-style: normal;
    white-space: nowrap;
  }
  .contact {
    position: absolute;
    right: 135px;
    top: 475px;
    margin: 0;
    margin-right: -3.6px;
    text-align: right;
    font-size: 24px;
    line-height: 32px;
    letter-spacing: 3.6px;
    color: var(--text-light);
    white-space: nowrap;
  }
  .contact span, .address span { display: block; }
</style>
</head>
<body>
  <main class="card">
    <div class="stripe stripe--mid"></div>
    <div class="stripe stripe--light"></div>
    <div class="stripe stripe--dark"></div>
    <div class="band"></div>

    <h1 class="name">Marta Velard</h1>

    <address class="address">
      <span>Address to be determined</span>
      <span>New York, NY 10036</span>
    </address>

    <p class="contact">
      <span class="contact__title">Managing Director</span>
      <span class="contact__phone">(555)038-4172</span>
      <span class="contact__email">mvelard@callowayridgesearch.example</span>
    </p>
  </main>
</body>
</html>
```